Industrial Professional Business Card Design (Vantrel Systems)

Would like professional looking business cards. Not too busy leaning towards minimal. Should have a slogan like:
"Industrial Automation and Control".

We are a tech company that programs industrial PLC computers. We also develop custom hardware solutions. Please use the logo for inspiration.

Target Market(s)

Mining, industrial, processing, automation, factory

Industry/Entity Type

Engineering

Contact Information for Business Card

Name, phone, email, website. job title.

Font styles to use
Other font styles liked:
• droid sans

Requirements
Must have
• Use colours that go well with the logo. Not too busy design.

```html
<!DOCTYPE html>
<html lang="en">
<head>
<meta charset="utf-8">
<title>Vantrel Systems — Business Card</title>
<link href="https://fonts.googleapis.com/css2?family=Noto+Sans:wght@400;700&display=swap" rel="stylesheet">
<style>
  :root {
    --page: #e4e4e2;
    --card: #6e9fc6;
    --card-shade: #6597bf;
    --gear: #27679c;
    --gear-soft: rgba(39, 103, 156, 0.55);
    --text-light: #d9ecfa;
    --text-strong: #eef7ff;
    --brand-navy: #1f4274;
    --brand-orange: #ef6b22;
  }
  * { box-sizing: border-box; margin: 0; padding: 0; }
  html, body {
    width: 1200px;
    height: 900px;
    overflow: hidden;
    background: var(--page);
    font-family: "Noto Sans", "Droid Sans", sans-serif;
  }
  .sheet {
    position: relative;
    width: 1200px;
    height: 900px;
  }
  .card {
    position: absolute;
    left: 250px;
    width: 700px;
    height: 400px;
    background: linear-gradient(160deg, var(--card) 0%, var(--card-shade) 100%);
    overflow: hidden;
    box-shadow: 0 2px 6px rgba(0, 0, 0, 0.18);
  }
  .card--back { top: 35px; }
  .card--front { top: 465px; }

  .gear-field {
    position: absolute;
    border-radius: 50%;
  }

  /* back side */
  .card--back .gear-field--cluster {
    left: -60px;
    top: -40px;
    width: 300px;
    height: 260px;
    background: radial-gradient(circle, var(--gear-soft) 0%, rgba(39,103,156,0.25) 55%, rgba(39,103,156,0) 72%);
  }
  .card--back .gear-field--large {
    left: -40px;
    top: 250px;
    width: 260px;
    height: 240px;
    background: radial-gradient(circle, var(--gear-soft) 0%, rgba(39,103,156,0.25) 55%, rgba(39,103,156,0) 72%);
  }
  .slogan {
    position: absolute;
    top: 98px;
    left: 155px;
    right: 30px;
    text-align: center;
    font-weight: 700;
    font-size: 27px;
    letter-spacing: 0.5px;
    color: var(--text-light);
  }

  /* front side */
  .card--front .gear-field--right {
    right: -70px;
    top: -10px;
    width: 200px;
    height: 340px;
    background: radial-gradient(ellipse, var(--gear-soft) 0%, rgba(39,103,156,0.25) 55%, rgba(39,103,156,0) 72%);
  }
  .card--front .gear-field--left {
    left: -60px;
    top: 250px;
    width: 260px;
    height: 220px;
    background: radial-gradient(circle, var(--gear-soft) 0%, rgba(39,103,156,0.25) 55%, rgba(39,103,156,0) 72%);
  }
  .brand {
    position: absolute;
    top: 62px;
    left: 0;
    right: 0;
    display: flex;
    flex-direction: column;
    align-items: center;
    gap: 16px;
  }
  .brand__dot {
    width: 96px;
    height: 96px;
    border-radius: 50%;
    background: var(--brand-navy);
  }
  .brand__name {
    font-weight: 400;
    font-size: 50px;
    line-height: 1;
    color: var(--brand-navy);
    letter-spacing: 0.5px;
  }
  .contact {
    position: absolute;
    top: 238px;
    left: 0;
    right: 0;
    list-style: none;
    text-align: center;
    font-size: 19px;
    line-height: 27px;
    color: var(--text-light);
  }
  .contact__value {
    font-weight: 700;
    color: var(--text-strong);
  }
</style>
</head>
<body>
<main class="sheet">
  <section class="card card--back" aria-label="Card back">
    <div class="gear-field gear-field--cluster" role="img" aria-label="Cluster of interlocking gear outlines in dark blue"></div>
    <div class="gear-field gear-field--large" role="img" aria-label="Large gear outline rising from the bottom edge"></div>
    <p class="slogan">Industrial Automation and Control</p>
  </section>

  <section class="card card--front" aria-label="Card front">
    <div class="gear-field gear-field--right" role="img" aria-label="Column of gear outlines along the right edge"></div>
    <div class="gear-field gear-field--left" role="img" aria-label="Gear outlines in the lower left corner"></div>
    <div class="brand">
      <span class="brand__dot"></span>
      <span class="brand__name">Vantrel Systems</span>
    </div>
    <ul class="contact">
      <li>Name: <span class="contact__value">John Smith</span></li>
      <li>Phone: <span class="contact__value">123-456-7890</span></li>
      <li>Email: <span class="contact__value">someone@example.com</span></li>
      <li>Website: <span class="contact__value">someone.com</span></li>
      <li>Title: <span class="contact__value">Job Title</span></li>
    </ul>
  </section>
</main>
</body>
</html>
```